Bref créative
Business Cards and Stationery for The Cheerful Parcel
The Cheerful Parcel
Traditional
Nora Whitcomb
Chief Executive Officer
24817 Halvern
Dunmore, MI 4735-1186
nora@thecheerfulparcel.example
www.thecheerfulparcel.example
This is my logo in AI

```html
<!DOCTYPE html>
<html lang="en">
<head>
<meta charset="utf-8">
<title>The Cheerful Parcel — Business Card</title>
<link rel="stylesheet" href="https://fonts.googleapis.com/css2?family=Open+Sans:wght@400;600;700&display=swap">
<style>
  :root {
    --backdrop: #ecebe8;
    --card-purple: #6e1466;
    --band-pink: #f4aeb1;
    --accent-pink: #f6a9ad;
    --text-white: #ffffff;
    --text-soft: #f3e4f1;
    --icon-purple: #6e1466;
  }
  * { margin: 0; padding: 0; box-sizing: border-box; }
  html, body {
    width: 1200px; height: 900px; overflow: hidden;
    background: var(--backdrop);
    font-family: "Open Sans", Arial, sans-serif;
  }
  .business-card {
    position: absolute; left: 100px; top: 165px;
    width: 1000px; height: 571px;
    background: var(--card-purple);
    box-shadow: 0 10px 30px rgba(0,0,0,0.18);
    overflow: hidden;
  }
  .brand {
    position: absolute; left: 48px; top: 70px;
    display: flex; align-items: center; gap: 16px;
  }
  .brand-dot {
    width: 30px; height: 30px; border-radius: 50%;
    background: var(--accent-pink);
  }
  .brand-name {
    color: var(--accent-pink);
    font-weight: 600; font-size: 40px; line-height: 1.15;
    width: 230px;
  }
  .tagline {
    position: absolute; left: 48px; top: 250px;
    color: var(--text-white);
    font-size: 19px; letter-spacing: 2px; font-weight: 400;
  }
  .person {
    position: absolute; left: 48px; top: 380px;
  }
  .person-marker {
    position: absolute; left: 0; top: 6px;
    width: 0; height: 0;
    border-top: 13px solid transparent;
    border-bottom: 13px solid transparent;
    border-left: 20px solid var(--text-white);
  }
  .person-name {
    margin-left: 34px;
    color: var(--accent-pink); font-weight: 700; font-size: 26px;
  }
  .person-title {
    margin-left: 34px;
    color: var(--text-white); font-size: 19px; margin-top: 2px;
  }
  .contact-list {
    position: absolute; left: 640px; top: 318px;
    list-style: none;
  }
  .contact-item {
    display: flex; align-items: flex-start; gap: 12px;
    color: var(--text-soft); font-size: 16px; line-height: 21px;
    margin-bottom: 7px;
  }
  .contact-icon {
    flex: 0 0 20px; width: 20px; height: 20px; margin-top: 1px;
  }
  .side-band {
    position: absolute; right: 0; top: 0;
    width: 52px; height: 100%;
    background: var(--band-pink);
  }
  .side-band-url {
    position: absolute; right: 26px; top: 30px;
    transform-origin: right top;
    transform: rotate(-90deg) translateY(-50%);
    transform: translateX(50%) rotate(90deg);
    transform-origin: center;
    white-space: nowrap;
    color: var(--card-purple); font-size: 15px; letter-spacing: 3px;
  }
  .side-band-url {
    right: auto; left: 26px; top: 40px;
    transform: translateX(-50%) translateX(0) rotate(90deg);
    transform-origin: 0 50%;
    left: 36px;
  }
</style>
</head>
<body>
  <main class="business-card">
    <div class="brand">
      <span class="brand-dot"></span>
      <span class="brand-name">The Cheerful Parcel</span>
    </div>
    <p class="tagline">Uplifting gifts for women</p>

    <div class="person">
      <span class="person-marker"></span>
      <p class="person-name">Nora Whitcomb</p>
      <p class="person-title">Chief Executive Officer</p>
    </div>

    <ul class="contact-list">
      <li class="contact-item">
        <svg class="contact-icon" viewBox="0 0 20 20"><circle cx="10" cy="10" r="10" fill="#fff"/><path d="M10 4a4 4 0 0 0-4 4c0 3 4 8 4 8s4-5 4-8a4 4 0 0 0-4-4zm0 5.5a1.5 1.5 0 1 1 0-3 1.5 1.5 0 0 1 0 3z" fill="var(--icon-purple)"/></svg>
        <span>24817 Halvern<br>Dunmore, MI 4735-1186</span>
      </li>
      <li class="contact-item">
        <svg class="contact-icon" viewBox="0 0 20 20"><circle cx="10" cy="10" r="10" fill="#fff"/><path d="M7 5l2 2.5-1.2 1.3a7 7 0 0 0 3.4 3.4L12.5 11 15 13l-1.2 1.8C10 15 5 10 5.2 6.2z" fill="var(--icon-purple)"/></svg>
        <span>734-555-0146</span>
      </li>
      <li class="contact-item">
        <svg class="contact-icon" viewBox="0 0 20 20"><circle cx="10" cy="10" r="10" fill="#fff"/><circle cx="10" cy="10" r="5" fill="var(--icon-purple)"/></svg>
        <span>3135550182</span>
      </li>
      <li class="contact-item">
        <svg class="contact-icon" viewBox="0 0 20 20"><circle cx="10" cy="10" r="10" fill="#fff"/><rect x="6" y="8" width="8" height="6" fill="var(--icon-purple)"/><rect x="7.5" y="5" width="5" height="3" fill="var(--icon-purple)"/></svg>
        <span>734-555-0197</span>
      </li>
      <li class="contact-item">
        <svg class="contact-icon" viewBox="0 0 20 20"><circle cx="10" cy="10" r="10" fill="#fff"/><rect x="5" y="6.5" width="10" height="7" fill="var(--icon-purple)"/><path d="M5 6.5l5 4 5-4" stroke="#fff" stroke-width="1" fill="none"/></svg>
        <span>nora@thecheerfulparcel.example</span>
      </li>
      <li class="contact-item">
        <svg class="contact-icon" viewBox="0 0 20 20"><circle cx="10" cy="10" r="10" fill="#fff"/><circle cx="10" cy="10" r="5" fill="none" stroke="var(--icon-purple)" stroke-width="1.4"/><path d="M5 10h10M10 5c-2 3-2 7 0 10M10 5c2 3 2 7 0 10" stroke="var(--icon-purple)" stroke-width="1" fill="none"/></svg>
        <span>www.thecheerfulparcel.example</span>
      </li>
    </ul>

    <aside class="side-band">
      <span class="side-band-url">www.thecheerfulparcel.example</span>
    </aside>
  </main>
</body>
</html>
```